Single brochure for international companies in the financial sector

We need to update a brochure 4 pages presenting our company. We are a financial engineering company. The final design must provide financial security, service and trust. you will find the current brochure copy. Our color code is Orange (RGB 235/100/68), Black, White and Gray. photos show the visual of the site, but it is not mandatory to keep them.

Target Market(s)

wealth management professionals

Industry/Entity Type

Finance

Requirements
Must have
• Logo Tolvane Capital all text in the document color Orange Tolvane (RGB 235/100/68)
Nice to have
• Vista Font
Should not have
• images / pictures of people

```html
<!DOCTYPE html>
<html lang="en">
<head>
<meta charset="utf-8">
<title>Tolvane Capital – Company Brochure Spread</title>
<link href="https://fonts.googleapis.com/css2?family=Questrial&display=swap" rel="stylesheet">
<style>
  :root {
    --orange: #eb6444;
    --ink: #3a3a3a;
    --muted: #6b6b6b;
    --rule: #c9c9c9;
    --paper: #ffffff;
    --backdrop: #dcdcdc;
    --photo-light: #c4c0bc;
    --photo-dark: #6f6a66;
  }
  * { box-sizing: border-box; margin: 0; padding: 0; }
  html, body {
    width: 1200px; height: 847px; overflow: hidden;
    background: var(--backdrop);
    font-family: "Questrial", "Century Gothic", sans-serif;
    color: var(--ink);
  }
  .spread {
    position: absolute; left: 60px; top: 94px;
    width: 1080px; height: 660px;
    display: flex;
  }
  .page {
    position: relative; width: 540px; height: 660px;
    background: var(--paper);
    padding: 34px 30px 30px;
  }
  .page--left { border-right: 1px solid #e4e4e4; }
  .page-header {
    display: flex; align-items: flex-end; gap: 12px;
    margin-bottom: 10px;
  }
  .page-title {
    color: var(--orange); font-size: 19px; font-weight: 400;
    letter-spacing: 0.5px; white-space: nowrap; line-height: 1;
  }
  .page-header__bar {
    flex: 1; height: 6px; background: var(--orange); margin-bottom: 7px;
    margin-right: -30px;
  }
  .page--left .page-header__bar { margin-right: -30px; }
  .photo {
    display: block; width: 100%;
  }
  .photo--street {
    height: 290px;
    background: linear-gradient(135deg, var(--photo-light) 0%, #9e9893 55%, var(--photo-dark) 100%);
    margin-left: -30px; width: calc(100% + 30px);
  }
  .photo--arch {
    height: 250px;
    background: linear-gradient(160deg, #f2f2f2 0%, #cfcfcf 40%, #5c5c5c 100%);
    margin-right: -30px; width: calc(100% + 30px);
  }
  .columns { display: flex; gap: 0; margin-top: 22px; }
  .column { flex: 1; padding: 0 16px; }
  .column:first-child { padding-left: 0; }
  .column:last-child { padding-right: 0; }
  .column + .column { border-left: 1px solid var(--rule); }
  .section-title {
    color: var(--orange); font-size: 12.5px; font-weight: 400;
    padding-bottom: 4px; border-bottom: 1px solid var(--orange);
    margin-bottom: 8px; letter-spacing: 0.3px;
  }
  .section + .section { margin-top: 22px; }
  .body-text {
    font-size: 10.5px; line-height: 1.35; color: var(--ink);
    text-align: justify;
  }
  .body-text + .body-text { margin-top: 8px; }
  .pull-quote {
    position: absolute; right: 0; bottom: 0;
    width: 258px; height: 120px;
    background: var(--orange); color: #fff;
    padding: 22px 22px 16px 26px;
    font-size: 12px; line-height: 1.4; font-style: italic;
  }
  .pull-quote__mark {
    position: absolute; font-size: 20px; font-style: normal; line-height: 1;
  }
  .pull-quote__mark--open { left: 12px; top: 8px; }
  .pull-quote__mark--close { right: 12px; bottom: 8px; }
  .pull-quote p + p { margin-top: 6px; }
  .partner { margin-top: 26px; }
</style>
</head>
<body>
  <main class="spread">
    <section class="page page--left">
      <header class="page-header">
        <h1 class="page-title">THE COMPANY</h1>
        <span class="page-header__bar"></span>
      </header>
      <div class="photo photo--street" role="img" aria-label="Black and white photograph of cobblestone street with tram rails"></div>

      <div class="columns">
        <div class="column">
          <article class="section">
            <h2 class="section-title">ABOUT US:</h2>
            <p class="body-text">Tolvane Capital is a financial engineering company.</p>
            <p class="body-text">It is fully independent from any bank or any other company.</p>
          </article>
          <article class="section">
            <h2 class="section-title">WHAT WE DO</h2>
            <p class="body-text">We provide them with investment solutions designed to improve their portfolios performance.</p>
            <p class="body-text">Simple as that.</p>
          </article>
        </div>
        <div class="column">
          <article class="section">
            <h2 class="section-title">OUR CLIENTS:</h2>
            <p class="body-text">Our clients are financial professionals such as asset managers, institutionnals, corporates, private banks, wealth managers and family offices.</p>
            <p class="body-text">Our purpose is to make their work easier, every day.</p>
          </article>
        </div>
      </div>

      <blockquote class="pull-quote">
        <span class="pull-quote__mark pull-quote__mark--open">&ldquo;</span>
        <p>Our Clients must deliver performance on their portfolio on a regular basis.</p>
        <p>We help them deliver everyday.</p>
        <span class="pull-quote__mark pull-quote__mark--close">&rdquo;</span>
      </blockquote>
    </section>

    <section class="page page--right">
      <header class="page-header">
        <h1 class="page-title">OUR SERVICES</h1>
        <span class="page-header__bar"></span>
      </header>
      <div class="photo photo--arch" role="img" aria-label="Black and white photograph of a stone aqueduct arch against the sky"></div>

      <div class="columns">
        <div class="column">
          <article class="section">
            <h2 class="section-title">INVESTMENT ADVICE</h2>
            <p class="body-text">Each client is looking for a unique investment solution. Hence, we combine internal and external resources to create the financial product that will best fit our clients requirements.</p>
            <p class="body-text">Thanks to a truly independent advice, we offer bespoke, simple and efficient solutions.</p>
          </article>
        </div>
        <div class="column">
          <article class="section">
            <h2 class="section-title">PORTFOLIO ANALYSIS</h2>
            <p class="body-text">We advise our clients on their portfolios of financial products. Together we identify the needs for restructuring or reallocating the assets.</p>
            <p class="body-text">We also provide full monitoring and reporting services throughout the life of the products.</p>
          </article>
        </div>
      </div>

      <article class="section partner">
        <h2 class="section-title" style="width:240px">PARTNER SELECTION</h2>
        <p class="body-text">Our internal tools allow us to continuously assess the issuers we are working with. Therefore we give our clients the luxury to chose among the best issuers for their investment solution.</p>
      </article>
    </section>
  </main>
</body>
</html>
```